Business Card Design

Electronic Security
Alarm Systems
CCTV
Electronic Access Control
Security System Integration

Industry/Entity Type

Business

Contact Information for Business Card

Declan Whitfield
PO Box 862
Carrowbrook Qld 4179
Phone 07 38265014
Mob 0428615937

```html
<!DOCTYPE html>
<html lang="en">
<head>
<meta charset="utf-8">
<title>Business Card – Declan Whitfield</title>
<link href="https://fonts.googleapis.com/css2?family=Arimo:wght@400;700&display=swap" rel="stylesheet">
<style>
  :root {
    --backdrop: #2b2b2d;
    --card-white: #ffffff;
    --sun-yellow: #f2b613;
    --sun-yellow-deep: #e0a20c;
    --sky-blue: #1e9ad6;
    --slate: #2f3a48;
    --ink: #111111;
  }
  html, body {
    margin: 0;
    width: 1200px;
    height: 997px;
    overflow: hidden;
    background: var(--backdrop);
  }
  .card {
    position: absolute;
    left: 150px;
    top: 241px;
    width: 900px;
    height: 514px;
    background: var(--card-white);
    box-shadow: 0 18px 40px rgba(0,0,0,.55);
    overflow: hidden;
    font-family: "Arimo", Arial, sans-serif;
  }
  .card-shapes {
    position: absolute;
    inset: 0;
  }
  .holder-name {
    position: absolute;
    left: 34px;
    top: 158px;
    margin: 0;
    color: #fff;
    font-size: 30px;
    font-weight: 700;
    letter-spacing: .3px;
  }
  .contact-list {
    position: absolute;
    left: 34px;
    top: 222px;
    margin: 0;
    padding: 0;
    list-style: none;
    color: var(--ink);
    font-size: 26px;
    font-weight: 700;
    letter-spacing: 1px;
  }
  .contact-list li {
    display: flex;
    align-items: center;
    gap: 18px;
    height: 38px;
  }
  .contact-list svg { width: 22px; height: 22px; }
  .services-title {
    position: absolute;
    left: 34px;
    top: 318px;
    margin: 0;
    color: var(--sky-blue);
    font-size: 25px;
    font-weight: 700;
  }
  .services-list {
    position: absolute;
    left: 34px;
    top: 356px;
    margin: 0;
    padding: 0;
    list-style: none;
    color: var(--ink);
    font-size: 20px;
    font-weight: 700;
    line-height: 29px;
  }
  .services-list li::before { content: "• "; }
  .brand {
    position: absolute;
    right: 70px;
    top: 300px;
    display: flex;
    align-items: center;
    gap: 16px;
  }
  .brand-dot {
    width: 46px;
    height: 46px;
    border-radius: 50%;
    background: var(--sky-blue);
  }
  .brand-name {
    color: var(--slate);
    font-size: 60px;
    font-weight: 400;
    letter-spacing: 2px;
  }
</style>
</head>
<body>
  <article class="card">
    <svg class="card-shapes" viewBox="0 0 900 514" width="900" height="514" aria-hidden="true">
      <defs>
        <linearGradient id="fold-shade" x1="0" y1="0" x2="1" y2="0">
          <stop offset="0" stop-color="#1a2430"/>
          <stop offset="1" stop-color="#3d4b5c"/>
        </linearGradient>
        <linearGradient id="yellow-fill" x1="0" y1="0" x2="0" y2="1">
          <stop offset="0" stop-color="#f6bd18"/>
          <stop offset="1" stop-color="#e3a60e"/>
        </linearGradient>
      </defs>
      <polygon points="0,0 360,0 520,514 0,514" fill="url(#yellow-fill)"/>
      <polygon points="0,148 318,148 286,200 0,200" fill="var(--sky-blue)"/>
      <polygon points="345,0 410,0 318,148 286,148" fill="var(--sky-blue)"/>
      <polygon points="318,148 360,0 405,0 560,514 515,514" fill="url(#fold-shade)"/>
    </svg>

    <h1 class="holder-name">Declan Whitfield</h1>

    <ul class="contact-list">
      <li>
        <svg viewBox="0 0 24 24" aria-label="Phone"><path d="M3 9c0-3 4-4 9-4s9 1 9 4v2h-5V9H8v2H3z M6 12h12l2 8H4z" fill="#111"/></svg>
        0738265014
      </li>
      <li>
        <svg viewBox="0 0 24 24" aria-label="Mobile"><rect x="6" y="2" width="12" height="20" rx="2" fill="none" stroke="#111" stroke-width="2"/></svg>
        0428615937
      </li>
    </ul>

    <h2 class="services-title">Our Services</h2>
    <ul class="services-list">
      <li>CCTV</li>
      <li>Alarm Systems</li>
      <li>Electronic Security</li>
      <li>Electronic Access Control</li>
      <li>Security System Integration</li>
    </ul>

    <div class="brand">
      <span class="brand-dot"></span>
      <span class="brand-name">Halden</span>
    </div>
  </article>
</body>
</html>
```